Clean, creative business Wordpress Site

Our company is building a website via Wordpress and needs a clean, no fuss, modern looking design that reflects our company brand (see attached logos).

In addition, the company is a woman owned business (no middle-aged white guy stock photos please) and primarily works with the oil & gas industry. We would prefer no images with direct references to energy (rigs, windmills, solar panels, etc.). Part of our consulting is providing thought leadership around energy politics and policy so creative ways to incorporate that visually will be appreciated as well.

Site map of pages below:

Home
- About
- Team
- Expertise
- Blog

We prefer a header image that includes the company logo and easy to identify and navigate menus.

Target Market(s)

Energy professionals, Executives

Industry/Entity Type

Consulting

Font styles to use
Serif

Colors
85acd3
0255a3
cedeed
ffffff

Requirements
Must have
• Clean and easy to navigate, clear menus, simple design that reflects company logo.

```html
<!DOCTYPE html>
<html lang="en">
<head>
<meta charset="utf-8">
<title>Veridane Energy</title>
<link href="https://fonts.googleapis.com/css2?family=Montserrat:wght@300;400;500;600;700&display=swap" rel="stylesheet">
<style>
:root{
  --blue:#0255a3;
  --sky:#85acd3;
  --mist:#cedeed;
  --white:#ffffff;
  --ink:#222428;
  --text:#6a6d72;
  --grey-band:#efefef;
  --card:#f4f4f4;
  --card-line:#e2e2e2;
}
*{box-sizing:border-box;margin:0;padding:0}
html,body{width:1200px;height:2655px;overflow:hidden}
body{font-family:"Montserrat",Arial,sans-serif;color:var(--ink);background:var(--white)}
.wrap{width:888px;margin:0 auto;position:relative}

/* hero */
.hero{height:480px;position:relative;overflow:hidden}
.hero-photo{position:absolute;inset:0;background:linear-gradient(180deg,#2f73c9 0%,#4a8ad6 38%,#27579a 62%,#3c78bf 100%)}
.hero-photo::after{content:"";position:absolute;inset:0;background:rgba(2,85,163,.28)}
.topbar{position:absolute;top:18px;left:156px;right:156px;display:flex;justify-content:space-between;align-items:center;z-index:2}
.brand{display:flex;align-items:center;gap:12px;color:var(--white);font-weight:600;font-size:27px;letter-spacing:.5px}
.brand-mark{width:44px;height:44px;border:2px solid var(--white);border-radius:50%}
.nav{display:flex;gap:8px;align-items:center}
.nav a{color:var(--white);text-decoration:none;font-size:13px;padding:7px 17px;border-radius:20px;border:2px solid transparent}
.nav a.active{border-color:var(--white)}
.hero-copy{position:absolute;top:218px;left:0;right:0;text-align:center;color:var(--white);z-index:2}
.hero-copy h2{font-weight:400;font-size:30px;margin-bottom:8px}
.hero-copy h1{font-weight:600;font-size:30px}
.btn-ghost{display:inline-block;margin-top:30px;padding:7px 26px;border:1.5px solid var(--white);border-radius:20px;color:var(--white);font-size:12px}
.hero-arrow{position:absolute;top:222px;width:28px;height:32px;border:1.5px solid var(--white);z-index:2;display:flex;align-items:center;justify-content:center}
.hero-arrow.prev{left:104px}.hero-arrow.next{right:104px}

/* shared heading */
.section-title{display:flex;align-items:center;font-size:29px;font-weight:300;color:#5f86ae}
.section-title::before{content:"";width:76px;height:1.5px;background:var(--sky);margin-right:20px;flex:none}
.section-title b{font-weight:600;color:var(--sky)}

/* about */
.about{height:377px;padding-top:46px}
.about .wrap{display:flex;gap:52px}
.about-photo{width:380px;height:281px;background:linear-gradient(135deg,#d9dde3,#a7b1bd 60%,#6c7886);flex:none}
.about-body{padding-top:8px}
.about .section-title{margin-bottom:26px}
.about-body p{font-size:12px;line-height:18.5px;color:var(--text);width:456px}
.btn{display:inline-block;padding:8px 24px;border-radius:20px;font-size:11.5px;font-weight:500}
.btn-solid{background:var(--blue);color:var(--white)}
.btn-line{border:1.5px solid #9aa0a6;color:#7d8288}
.about .btn{margin-top:28px}

/* expertise */
.expertise{height:529px;background:var(--grey-band);padding-top:42px}
.heading-row{display:flex;justify-content:space-between;align-items:center}
.pager{display:flex;gap:6px;align-items:center;color:var(--ink);font-size:13px}
.cards{display:flex;justify-content:space-between;margin-top:29px}
.service{width:280px;height:378px;background:var(--card);border:1px solid var(--card-line);text-align:center}
.service.featured{box-shadow:0 4px 10px rgba(0,0,0,.2)}
.service-photo{height:182px}
.service h3{font-size:17px;font-weight:500;margin-top:22px}
.service h3::after{content:"";display:block;width:30px;height:2px;background:var(--sky);margin:10px auto 14px}
.service p{font-size:11.5px;line-height:18px;color:var(--text);padding:0 14px}
.service .btn{margin-top:24px;padding:7px 17px}

/* team + blog */
.people{height:869px;padding-top:45px}
.team{display:flex;justify-content:space-between;margin-top:25px}
.member{width:204px;height:246px;background:#eeeeee;text-align:center;padding-top:24px;position:relative}
.avatar{width:156px;height:156px;border-radius:50%;margin:0 auto;background:linear-gradient(160deg,#9aa4ae,#5e6872)}
.member h4{font-size:15px;font-weight:500;margin-top:14px}
.member span{font-size:11px;color:var(--blue);font-weight:500}
.member.featured{background:var(--blue);color:var(--white);box-shadow:6px -6px 0 -4px var(--white),6px -6px 0 -2.5px var(--blue)}
.member.featured .avatar{background:linear-gradient(160deg,#5c87c4,#3566a8);display:flex;align-items:center;justify-content:center}
.member.featured h4{margin-top:18px}
.member.featured span{color:var(--mist)}
.blog-title{margin-top:55px}
.posts{display:flex;justify-content:space-between;margin-top:20px}
.post{width:280px;height:374px;background:var(--white);border:1px solid #e6e6e6;box-shadow:0 1px 4px rgba(0,0,0,.08);position:relative}
.post-photo{height:184px;position:relative}
.post.featured .post-photo{background:linear-gradient(160deg,#2a6cb8,#0f4f98);display:flex;align-items:center;justify-content:center}
.link-chip{width:38px;height:38px;background:var(--white);border-radius:3px;display:flex;align-items:center;justify-content:center}
.date{position:absolute;left:24px;top:160px;width:48px;height:48px;background:#555758;color:var(--white);text-align:center;font-size:17px;line-height:20px;padding-top:5px}
.date small{display:block;font-size:12px;line-height:14px}
.post.featured .date{background:var(--blue)}
.post h5{font-size:12px;font-weight:600;line-height:17px;margin:34px 22px 10px}
.post p{font-size:11px;line-height:17px;color:var(--text);margin:0 22px}
.post .more{display:block;margin:14px 22px 0;font-size:11.5px;font-weight:600;color:#333}
.post.featured .more{color:var(--blue);text-decoration:underline}

/* contact */
.contact{height:350px;position:relative;overflow:hidden;color:var(--white)}
.contact-photo{position:absolute;inset:0;background:linear-gradient(180deg,#3a3026 0%,#221d19 55%,#151311 100%)}
.contact .wrap{padding-top:40px}
.contact .section-title{color:var(--white);font-weight:500}
.contact .section-title::before{background:var(--white)}
.contact .section-title b{color:var(--white);font-weight:600}
.contact-grid{display:flex;gap:46px;margin-top:30px}
.info{width:258px}
.info-item{display:flex;gap:12px;margin-bottom:20px}
.info-item svg{flex:none;margin-top:2px}
.info-item h6{font-size:14px;font-weight:500;margin-bottom:8px}
.info-item p{font-size:12px;line-height:18px;color:#ddd}
.info-item a{color:#ddd;text-decoration:underline}
.form{flex:1;display:grid;grid-template-columns:1fr 1fr;gap:20px 24px;align-content:start}
.field{border:1px solid rgba(255,255,255,.55);height:32px;font-size:12px;padding:8px 10px}
.field.message{grid-column:1/3;height:90px}
.send{display:inline-flex;align-items:center;gap:6px;background:var(--blue);color:var(--white);border-radius:20px;padding:8px 20px;font-size:12px;margin-top:-4px;width:max-content}

/* footer */
.footer{height:50px;background:#0e0e0e;color:#ddd;font-size:11.5px}
.footer .wrap{display:flex;justify-content:space-between;align-items:center;height:50px}
.social{display:flex;gap:14px}
.social i{width:14px;height:14px;border-radius:50%;background:#e6e6e6;display:block}
</style>
</head>
<body>

<header class="hero">
  <div class="hero-photo" role="img" aria-label="Rows of solar panels under a blue sky with white clouds"></div>
  <div class="topbar">
    <div class="brand"><span class="brand-mark"></span>Veridane Energy</div>
    <nav class="nav">
      <a class="active">Home</a><a>About</a><a>Team</a><a>Expertise</a><a>Blog</a><a>Contact Us</a>
    </nav>
  </div>
  <span class="hero-arrow prev"><svg width="14" height="14" viewBox="0 0 14 14"><path d="M9 2 4 7l5 5" fill="none" stroke="#fff" stroke-width="1.6"/></svg></span>
  <span class="hero-arrow next"><svg width="14" height="14" viewBox="0 0 14 14"><path d="M5 2l5 5-5 5" fill="none" stroke="#fff" stroke-width="1.6"/></svg></span>
  <div class="hero-copy">
    <h2>There are many variations of passages</h2>
    <h1>I must explain to you how all this mistaken idea</h1>
    <span class="btn-ghost">Explore More</span>
  </div>
</header>

<section class="about">
  <div class="wrap">
    <div class="about-photo" role="img" aria-label="Four colleagues meeting around a table in a bright office"></div>
    <div class="about-body">
      <h2 class="section-title"><span><b>About Us</b></span></h2>
      <p>There are many variations of passages of Lorem Ipsum available, but the majority have suffered alteration in some form, by injected humour, or randomised words which don't look even slightly believable. If you are going to use a passage of Lorem Ipsum, you need to be sure there isn't anything embarrassing hidden in the middle of text. All the Lorem Ipsum generators on the Internet tend to repeat predefined chunks as necessary, making this the first true generator on the Internet. It uses a dictionary of over 200 Latin words, combined with a handful of model...</p>
      <span class="btn btn-solid">Discover More</span>
    </div>
  </div>
</section>

<section class="expertise">
  <div class="wrap">
    <div class="heading-row">
      <h2 class="section-title"><span>Our <b>Expertise</b></span></h2>
      <div class="pager"><svg width="14" height="8" viewBox="0 0 14 8"><path d="M14 4H2M5 1 1 4l4 3" fill="none" stroke="#222" stroke-width="1.5"/></svg>/<svg width="14" height="8" viewBox="0 0 14 8"><path d="M0 4h12M9 1l4 3-4 3" fill="none" stroke="#0255a3" stroke-width="1.5"/></svg></div>
    </div>
    <div class="cards">
      <article class="service">
        <div class="service-photo" role="img" aria-label="Team gathered around a long conference table" style="background:linear-gradient(150deg,#e7d9c4,#b9a48a 55%,#7e6d5c)"></div>
        <h3>Community Engagement</h3>
        <p>Lorem Ipsum passages, and more recently with desktop publishing software like Pagewright Studio including versions...</p>
        <span class="btn btn-line">Read More</span>
      </article>
      <article class="service featured">
        <div class="service-photo" role="img" aria-label="Colleagues talking around a laptop in a light office" style="background:linear-gradient(150deg,#dfeaf6,#a9c3df 55%,#6e8fb4)"></div>
        <h3>Deescalating Conflict</h3>
        <p>Lorem Ipsum passages, and more recently with desktop publishing software like Pagewright Studio including versions...</p>
        <span class="btn btn-solid">Read More</span>
      </article>
      <article class="service">
        <div class="service-photo" role="img" aria-label="Power plant and transmission towers reflected in water at sunset" style="background:linear-gradient(180deg,#6d8fc0,#b7c9e2 45%,#2f4f7e 70%,#1d355a)"></div>
        <h3>Energy Access</h3>
        <p>Lorem Ipsum passages, and more recently with desktop publishing software like Pagewright Studio including versions...</p>
        <span class="btn btn-line">Read More</span>
      </article>
    </div>
  </div>
</section>

<section class="people">
  <div class="wrap">
    <div class="heading-row">
      <h2 class="section-title"><span>Our <b>Team</b></span></h2>
      <div class="pager"><svg width="14" height="8" viewBox="0 0 14 8"><path d="M14 4H2M5 1 1 4l4 3" fill="none" stroke="#222" stroke-width="1.5"/></svg>/<svg width="14" height="8" viewBox="0 0 14 8"><path d="M0 4h12M9 1l4 3-4 3" fill="none" stroke="#0255a3" stroke-width="1.5"/></svg></div>
    </div>
    <div class="team">
      <div class="member"><div class="avatar" role="img" aria-label="Portrait of a team member in a suit"></div><h4>Marlo Quentin</h4><span>Manager</span></div>
      <div class="member featured"><div class="avatar" role="img" aria-label="Portrait of a team member"><svg width="22" height="22" viewBox="0 0 22 22"><g fill="none" stroke="#fff" stroke-width="2.4"><rect x="3" y="9" width="9" height="5" rx="2.5" transform="rotate(-45 7.5 11.5)"/><rect x="10" y="8" width="9" height="5" rx="2.5" transform="rotate(-45 14.5 10.5)"/></g></svg></div><h4>Finibus Bonorum</h4><span>Founder</span></div>
      <div class="member"><div class="avatar" role="img" aria-label="Portrait of a team member in a checked shirt"></div><h4>Deleniti Atque</h4><span>Managing Director</span></div>
      <div class="member"><div class="avatar" role="img" aria-label="Portrait of a team member in a white shirt"></div><h4>Corrupti Quos</h4><span>Assistant Manager</span></div>
    </div>

    <h2 class="section-title blog-title"><span>Our <b>Blog</b></span></h2>
    <div class="posts">
      <article class="post">
        <div class="post-photo" role="img" aria-label="White canopy tent with equipment outdoors" style="background:linear-gradient(180deg,#7b9160,#b9bcae 50%,#9a9486)"></div>
        <div class="date">10<small>Jun</small></div>
        <h5>Lorem Ipsum is therefore always free from repetition, injected</h5>
        <p>There are many variations of passages of Lorem Ipsum available, but the majority have suffered alteration in some form...</p>
        <span class="more">Read More &raquo;</span>
      </article>
      <article class="post featured">
        <div class="post-photo" role="img" aria-label="Outdoor work site under a blue overlay"><span class="link-chip"><svg width="16" height="16" viewBox="0 0 22 22"><g fill="none" stroke="#0255a3" stroke-width="2.4"><rect x="3" y="9" width="9" height="5" rx="2.5" transform="rotate(-45 7.5 11.5)"/><rect x="10" y="8" width="9" height="5" rx="2.5" transform="rotate(-45 14.5 10.5)"/></g></svg></span></div>
        <div class="date">17<small>Jun</small></div>
        <h5>Lorem Ipsum is therefore always free from repetition, injected</h5>
        <p>There are many variations of passages of Lorem Ipsum available, but the majority have suffered alteration in some form...</p>
        <span class="more">Read More &raquo;</span>
      </article>
      <article class="post">
        <div class="post-photo" role="img" aria-label="Paved stone patio with outdoor furniture" style="background:linear-gradient(180deg,#5a4a3c,#a49a8e 45%,#c8c1b6)"></div>
        <div class="date">15<small>Aug</small></div>
        <h5>Lorem Ipsum is therefore always free from repetition, injected</h5>
        <p>There are many variations of passages of Lorem Ipsum available, but the majority have suffered alteration in some form...</p>
        <span class="more">Read More &raquo;</span>
      </article>
    </div>
  </div>
</section>

<section class="contact">
  <div class="contact-photo" role="img" aria-label="Silhouette of electricity pylons against a dusky sky"></div>
  <div class="wrap">
    <h2 class="section-title"><span>Contact <b>Us</b></span></h2>
    <div class="contact-grid">
      <div class="info">
        <div class="info-item">
          <svg width="14" height="18" viewBox="0 0 14 18"><path d="M7 0a7 7 0 0 0-7 7c0 5 7 11 7 11s7-6 7-11a7 7 0 0 0-7-7zm0 10a3 3 0 1 1 0-6 3 3 0 0 1 0 6z" fill="#fff"/></svg>
          <div><h6>Address :</h6><p>Sed ut perspiciatis unde omnis iste commodi consequatur 123450</p></div>
        </div>
        <div class="info-item">
          <svg width="16" height="16" viewBox="0 0 16 16"><path d="M3.5 0 6 4 4.3 5.7a10 10 0 0 0 6 6L12 10l4 2.5-1.5 3C7 16 0 9 .5 1.5z" fill="#fff"/></svg>
          <div><h6>Phone :</h6><p>123-456-7890</p></div>
        </div>
        <div class="info-item">
          <svg width="16" height="12" viewBox="0 0 16 12"><rect width="16" height="12" rx="1.5" fill="#fff"/><path d="M1 1.5 8 7l7-5.5" fill="none" stroke="#222" stroke-width="1.3"/></svg>
          <div><h6>Email :</h6><p><a>info@veridaneenergy.com</a></p></div>
        </div>
      </div>
      <div class="form">
        <div class="field">Name :</div>
        <div class="field">Email :</div>
        <div class="field message">Message :</div>
        <div class="send"><svg width="12" height="12" viewBox="0 0 12 12"><path d="M12 0 0 5l4 2 1 5 2-3 3 2z" fill="#fff"/></svg>Send</div>
      </div>
    </div>
  </div>
</section>

<footer class="footer">
  <div class="wrap">
    <span>Copyright &copy; 2016. &nbsp;Veridane Energy.</span>
    <div class="social"><i></i><i></i><i></i></div>
  </div>
</footer>

</body>
</html>
```